Simple Business Cards for Self-employed Coach

Simple business card with a design that includes the QLT logo.
Using either only the logo color or additional colors that match the logo.

Meridian Guides reach deeply into the past, gathering wisdom from East and West, while still staying current with the frontiers of new discovery in cognitive science, genetics, and other disciplines. see https://www.brightharborpath.example/what-is-integral-coaching/

Target Market(s)

Coaching Clients in Tokyo /Asia; in business organizations, but also outside

Industry/Entity Type

Life Coaching

Contact Information for Business Card

Lukas Brenning
Certified Meridian Guide

3-2-48 Kamiyoshi
Nakarino 164-0392
Tokyo, Japan

Phone: +81 70 4817 5062
E-Mail: lukas.brenning@mailora.example

Font styles to use
Sans Serif

Colors
00a990

Requirements
Must have
• include uploaded logo
• color fitting with QLT logo color
Nice to have
• simple, elegant design
Should not have
• clutter

```html
<!DOCTYPE html>
<html lang="en">
<head>
<meta charset="utf-8">
<title>Lukas Brenning – Business Card</title>
<link href="https://fonts.googleapis.com/css2?family=Open+Sans:wght@400;600&display=swap" rel="stylesheet">
<style>
  :root {
    --teal: #0d7d70;
    --text-grey: #767676;
    --card-white: #ffffff;
    --divider: #e6e6e6;
    --backdrop: #ebe8e4;
  }
  * { margin: 0; padding: 0; box-sizing: border-box; }
  html, body {
    width: 1200px;
    height: 1000px;
    overflow: hidden;
    background: var(--backdrop);
    font-family: "Open Sans", sans-serif;
  }
  .card {
    position: absolute;
    left: 266px;
    width: 666px;
    height: 397px;
    background: var(--card-white);
    box-shadow: 0 2px 8px rgba(0, 0, 0, 0.12);
  }
  .card--front { top: 74px; }
  .card--second { top: 533px; }

  .brand {
    position: absolute;
    left: 56px;
    top: 160px;
    display: flex;
    align-items: center;
    gap: 14px;
  }
  .brand__square {
    width: 26px;
    height: 26px;
    background: var(--teal);
  }
  .brand__name {
    font-size: 48px;
    font-weight: 600;
    letter-spacing: 6px;
    color: var(--teal);
    line-height: 1;
  }

  .divider {
    position: absolute;
    left: 333px;
    top: 105px;
    width: 1px;
    height: 182px;
    background: var(--divider);
  }

  .contact {
    position: absolute;
    left: 372px;
    top: 104px;
    color: var(--text-grey);
    font-size: 16px;
    line-height: 21px;
  }
  .contact__name {
    font-size: 21px;
    font-weight: 600;
    color: var(--teal);
    text-transform: uppercase;
    line-height: 26px;
  }
  .contact__role { margin-bottom: 12px; }
  .contact__address { margin-bottom: 12px; }
  .contact__line {
    display: flex;
    align-items: center;
    gap: 8px;
    line-height: 24px;
  }
  .contact__icon { width: 15px; height: 15px; flex: none; }
</style>
</head>
<body>

  <section class="card card--front">
    <div class="brand">
      <span class="brand__square"></span>
      <span class="brand__name">QLT</span>
    </div>
    <div class="divider"></div>
    <div class="contact">
      <p class="contact__name">Lukas Brenning</p>
      <p class="contact__role">Certified Meridian Guide</p>
      <p class="contact__address">3-2-48 Kamiyoshi<br>Nakarino 164-0392<br>Tokyo, Japan</p>
      <p class="contact__line">
        <svg class="contact__icon" viewBox="0 0 16 16" aria-hidden="true"><path fill="var(--teal)" d="M3.5 1.5l2.5 0 1 3.5-1.6 1.2c.8 1.8 2.2 3.2 4 4l1.2-1.6 3.5 1v2.5c0 .8-.7 1.4-1.5 1.4C6.9 13.5 2.1 8.7 2.1 3c0-.8.6-1.5 1.4-1.5z"/></svg>
        +81 70 4817 5062
      </p>
      <p class="contact__line">
        <svg class="contact__icon" viewBox="0 0 16 16" aria-hidden="true"><rect x="1" y="3.5" width="14" height="9" fill="var(--teal)"/><path d="M1.5 4l6.5 5 6.5-5" fill="none" stroke="#fff" stroke-width="1.2"/></svg>
        lukas.brenning@mailora.example
      </p>
    </div>
  </section>

  <section class="card card--second">
    <div class="brand">
      <span class="brand__square"></span>
      <span class="brand__name">QLT</span>
    </div>
    <div class="divider"></div>
    <div class="contact">
      <p class="contact__name">Lukas Brenning</p>
      <p class="contact__role">Certified Meridian Guide</p>
      <p class="contact__address">3-2-48 Kamiyoshi<br>Nakarino 164-0392<br>Tokyo, Japan</p>
      <p class="contact__line">
        <svg class="contact__icon" viewBox="0 0 16 16" aria-hidden="true"><path fill="var(--teal)" d="M3.5 1.5l2.5 0 1 3.5-1.6 1.2c.8 1.8 2.2 3.2 4 4l1.2-1.6 3.5 1v2.5c0 .8-.7 1.4-1.5 1.4C6.9 13.5 2.1 8.7 2.1 3c0-.8.6-1.5 1.4-1.5z"/></svg>
        +81 70 4817 5062
      </p>
      <p class="contact__line">
        <svg class="contact__icon" viewBox="0 0 16 16" aria-hidden="true"><rect x="1" y="3.5" width="14" height="9" fill="var(--teal)"/><path d="M1.5 4l6.5 5 6.5-5" fill="none" stroke="#fff" stroke-width="1.2"/></svg>
        lukas.brenning@mailora.example
      </p>
    </div>
  </section>

</body>
</html>
```